Morvela Aesthetic Doctor

I require an elegant, luxurious looking business card for my aesthetic business. I am a doctor and that will set me aside from competitors. I am planning to provide home and spa based treatments to clients with high expectations. I have attached my logo.

```html
<!DOCTYPE html>
<html lang="en">
<head>
<meta charset="utf-8">
<title>Morvela Aesthetic Doctor – Business Cards</title>
<link href="https://fonts.googleapis.com/css2?family=Lato:wght@300;400;700&display=swap" rel="stylesheet">
<style>
  :root {
    --backdrop: #dcdcdc;
    --card: #2f2f30;
    --sky: #7cc6e0;
    --sky-deep: #5fb4d4;
    --ink: #f1ede4;
    --band-ink: #2f2f30;
  }
  html, body {
    margin: 0;
    width: 1200px;
    height: 787px;
    overflow: hidden;
    background: var(--backdrop);
    font-family: "Lato", sans-serif;
  }
  .card {
    position: absolute;
    top: 230px;
    width: 560px;
    height: 326px;
    background: var(--card);
    box-shadow: 0 6px 16px rgba(0,0,0,0.25);
    overflow: hidden;
  }
  .card--contact { left: 27px; }
  .card--services { left: 613px; }

  .brand {
    position: absolute;
    left: 34px;
    top: 104px;
    display: flex;
    align-items: center;
    gap: 12px;
    white-space: nowrap;
  }
  .brand-dot {
    flex: none;
    width: 40px;
    height: 40px;
    border-radius: 50%;
    background: var(--sky-deep);
  }
  .brand-name {
    margin: 0;
    font-weight: 300;
    color: var(--ink);
    font-size: 30px;
    line-height: 1;
    letter-spacing: 2px;
    text-transform: uppercase;
  }
  .brand-name span {
    display: block;
    font-size: 12px;
    letter-spacing: 3px;
    margin-top: 6px;
  }

  .divider {
    position: absolute;
    left: 272px;
    top: 78px;
    width: 1.5px;
    height: 150px;
    background: var(--sky);
  }

  .contact {
    position: absolute;
    left: 292px;
    top: 86px;
    color: var(--ink);
    white-space: nowrap;
  }
  .contact-name {
    margin: 0;
    font-size: 16px;
    font-weight: 400;
  }
  .contact-name strong {
    color: var(--sky);
    font-weight: 700;
  }
  .contact-credential {
    margin: 4px 0 12px;
    font-size: 11.5px;
    font-weight: 300;
  }
  .contact-list {
    list-style: none;
    margin: 0;
    padding: 0;
  }
  .contact-list li {
    display: flex;
    align-items: center;
    gap: 9px;
    margin-bottom: 6px;
    font-size: 13px;
    font-weight: 300;
  }
  .contact-list svg {
    width: 13px;
    height: 13px;
    flex: none;
  }
  .social {
    display: flex;
    gap: 5px;
    margin: 2px 0 0 150px;
  }
  .social span {
    width: 11px;
    height: 11px;
    border-radius: 50%;
    background: var(--sky);
  }

  .services {
    position: absolute;
    left: 292px;
    top: 86px;
    margin: 0;
    padding: 0;
    list-style: none;
    color: var(--ink);
    font-size: 13px;
    font-weight: 400;
    line-height: 1.55;
    white-space: nowrap;
  }
  .services li::before {
    content: "";
    display: inline-block;
    width: 5px;
    height: 5px;
    border-radius: 50%;
    background: var(--sky);
    margin-right: 8px;
    vertical-align: middle;
  }

  .band {
    position: absolute;
    left: 0;
    bottom: 0;
    width: 100%;
    height: 50px;
    background: var(--sky);
    display: flex;
    align-items: center;
    padding-left: 60px;
    box-sizing: border-box;
  }
  .band p {
    margin: 0;
    color: var(--band-ink);
    font-size: 13.5px;
    letter-spacing: 1.5px;
    text-transform: uppercase;
  }
</style>
</head>
<body>
  <main>
    <article class="card card--contact">
      <div class="brand">
        <div class="brand-dot"></div>
        <h1 class="brand-name">Morvela<span>Aesthetic Doctor</span></h1>
      </div>
      <div class="divider"></div>
      <section class="contact">
        <p class="contact-name"><strong>Dr Elena Varsk,</strong> MRCPCH MD</p>
        <p class="contact-credential">Australasian Diploma of Aesthetic Medicine</p>
        <ul class="contact-list">
          <li>
            <svg viewBox="0 0 24 24" fill="none" stroke="var(--sky)" stroke-width="2.2" stroke-linecap="round" stroke-linejoin="round"><path d="M5 3h4l2 5-3 2a12 12 0 0 0 6 6l2-3 5 2v4a2 2 0 0 1-2 2A17 17 0 0 1 3 5a2 2 0 0 1 2-2z"/></svg>
            0800 555 014
          </li>
          <li>
            <svg viewBox="0 0 24 24" fill="none" stroke="var(--sky)" stroke-width="2.2" stroke-linejoin="round"><rect x="3" y="5" width="18" height="14"/><path d="M3 5l9 8 9-8"/></svg>
            elena@morvela.co.nz
          </li>
          <li>
            <svg viewBox="0 0 24 24" fill="none" stroke="var(--sky)" stroke-width="2.2"><circle cx="12" cy="12" r="9"/><path d="M3 12h18M12 3c3 3 3 15 0 18M12 3c-3 3-3 15 0 18"/></svg>
            www.morvela.co.nz
          </li>
        </ul>
        <div class="social"><span></span><span></span></div>
      </section>
      <footer class="band"><p>Home and Spa Based Treatments</p></footer>
    </article>

    <article class="card card--services">
      <div class="brand">
        <div class="brand-dot"></div>
        <h2 class="brand-name">Morvela<span>Aesthetic Doctor</span></h2>
      </div>
      <div class="divider"></div>
      <ul class="services">
        <li>Dermal injectables</li>
        <li>Plasma facials</li>
        <li>Microneedling</li>
        <li>Skin boosters</li>
        <li>Excessive sweating</li>
        <li>Home and Spa Based Treatments</li>
      </ul>
      <footer class="band"><p>Home and Spa Based Treatments</p></footer>
    </article>
  </main>
</body>
</html>
```